Managed IT services business card design

We haven't needed a business card since the founding of the business in 2005. All our clients have been coming through word of mouth. And lately more and more existing clients are requesting for our business cards to pass on to their contacts in recommending us.
So we needing a business card design. We use various innovative solutions and methodologies to provide IT services to small businesses in managing their IT systems. Our role is the same as an in-house, full-time IT Manager for our clients, but outsourced. So we take care of all our clients' IT needs, just as an IT Manager would be expected to perform.
We have a holding website, which we're happy to leave for now. If we can use the same logo would be great - www.lomvex.com.au
Preferred colours are shades of are white, grey and black.
We pride our business with the following traits: proactive, good service, prompt response, trustworthy.
Target Market(s)
Small businesses of any industry
Industry/Entity Type
Business

```html
<!DOCTYPE html>
<html lang="en">
<head>
<meta charset="UTF-8">
<title>Lomvex — Business Card</title>
<link rel="stylesheet" href="https://fonts.googleapis.com/css2?family=Jura:wght@400;500;600&display=swap">
<style>
  :root {
    --backdrop: #e9e9e7;
    --card-light: #ffffff;
    --card-shade: #e4e4e4;
    --ink: #1e1e1e;
    --ink-soft: #4a4a4a;
    --band-dark: #333333;
    --band-grey: #9a9a9a;
    --icon: #ffffff;
  }
  * { box-sizing: border-box; margin: 0; padding: 0; }
  html, body {
    width: 1057px;
    height: 1200px;
    overflow: hidden;
    background: var(--backdrop);
    font-family: "Jura", sans-serif;
    color: var(--ink);
  }
  .sheet {
    position: relative;
    width: 1057px;
    height: 1200px;
  }
  .card {
    position: absolute;
    top: 215px;
    width: 440px;
    height: 770px;
    background: radial-gradient(ellipse at 40% 45%, var(--card-light) 0%, #f6f6f6 45%, var(--card-shade) 100%);
    box-shadow: 0 12px 30px rgba(0,0,0,0.18);
  }
  .card--front { left: 60px; }
  .card--back { left: 557px; }

  .brand {
    position: absolute;
    font-weight: 500;
    font-size: 54px;
    letter-spacing: 14px;
    color: var(--ink);
    white-space: nowrap;
  }
  .card--front .brand { top: 60px; left: 60px; }
  .card--back .brand {
    top: 50%;
    left: 50%;
    transform: translate(-50%, -50%);
    margin-left: 7px;
  }

  .band {
    position: absolute;
    right: 48px;
    width: 32px;
  }
  .band--dark { top: 0; height: 330px; background: var(--band-dark); }
  .band--grey { top: 330px; height: 160px; background: var(--band-grey); }
  .band-icon {
    position: absolute;
    left: 6px;
    width: 20px;
    height: 20px;
  }

  .person {
    position: absolute;
    right: 96px;
    top: 268px;
    text-align: right;
  }
  .person-name {
    font-size: 26px;
    font-weight: 600;
    letter-spacing: 1px;
  }
  .person-role {
    font-size: 13px;
    font-weight: 500;
    letter-spacing: 1.5px;
    color: var(--ink-soft);
    margin-top: 4px;
  }

  .contacts {
    position: absolute;
    right: 96px;
    top: 343px;
    list-style: none;
    text-align: right;
    font-size: 16px;
    font-weight: 500;
    color: var(--ink-soft);
  }
  .contacts li { height: 36px; line-height: 36px; }

  .address {
    position: absolute;
    right: 96px;
    top: 560px;
    text-align: right;
    font-style: normal;
    font-size: 24px;
    font-weight: 600;
    line-height: 1.4;
    letter-spacing: 0.5px;
  }
</style>
</head>
<body>
<main class="sheet">

  <section class="card card--front" aria-label="Card front">
    <div class="brand">lomvex</div>

    <div class="band band--dark"></div>
    <div class="band band--grey">
      <svg class="band-icon" style="top:17px" viewBox="0 0 20 20" aria-hidden="true">
        <path d="M5 2 L8 2 L9 6 L7 8 Q9 12 12 13 L14 11 L18 12 L18 15 Q17 18 14 18 Q3 16 2 5 Q2 2 5 2 Z" fill="var(--icon)"/>
      </svg>
      <svg class="band-icon" style="top:53px" viewBox="0 0 20 20" aria-hidden="true">
        <rect x="5" y="1" width="10" height="18" rx="2" fill="var(--icon)"/>
        <rect x="7" y="4" width="6" height="10" fill="var(--band-grey)"/>
        <circle cx="10" cy="16.5" r="1" fill="var(--band-grey)"/>
      </svg>
      <svg class="band-icon" style="top:89px" viewBox="0 0 20 20" aria-hidden="true">
        <rect x="1" y="4" width="18" height="12" fill="var(--icon)"/>
        <path d="M1 4 L10 11 L19 4" fill="none" stroke="var(--band-grey)" stroke-width="1.5"/>
      </svg>
      <svg class="band-icon" style="top:125px" viewBox="0 0 20 20" aria-hidden="true">
        <circle cx="10" cy="10" r="8.5" fill="none" stroke="var(--icon)" stroke-width="1.6"/>
        <ellipse cx="10" cy="10" rx="3.5" ry="8.5" fill="none" stroke="var(--icon)" stroke-width="1.4"/>
        <path d="M1.5 10 H18.5" stroke="var(--icon)" stroke-width="1.4"/>
      </svg>
    </div>

    <div class="person">
      <div class="person-name">DANIEL REED</div>
      <div class="person-role">GENERAL MANAGER</div>
    </div>

    <ul class="contacts">
      <li>012 555 0142</li>
      <li>012 555 0142</li>
      <li>hello@lomvex.com.au</li>
      <li>www.lomvex.com.au</li>
    </ul>

    <address class="address">
      42 Harbour Road<br>
      2nd level Tower West
    </address>
  </section>

  <section class="card card--back" aria-label="Card back">
    <div class="brand">lomvex</div>
  </section>

</main>
</body>
</html>
```